young adult fiction novel titled 'Chronicles of the Lanterns - The Heron's Vigil'

Introduction
Hello! Attached you will find a combination of my own amateurish attempts at graphic design and also pictures that have inspired me. With the obvious exception of the ‘Crown of Embers’ and ‘Keeper of the Wells’ stuff, I have purchased the other images so they are fair game to be used (contact me if you want the hi-res versions).
I hope that by showing you these, I might be able to convey what I’m looking for in a front cover and a website. I’d just like to make a few points that might also help you understand a little better.
1. The book is called ‘The Heron’s Vigil’. It is a 'knights of the round table' type story so I would like
2. My concept is 12 tales, each told by a member of the zodiac. I would like the first front cover to be designed in such a way that the following 11 can be thematically linked together. The Heron’s Vigil is obviously the Capricorn’s tale.
3. As Capricorn is an earth sign, I would like the colour scheme to be green and brown. I would also definitely like the motto to be ‘Bend the River Back’.
4. The name of the series will be ‘Chronicles of the Lanterns’ and I would like this written somewhere on the front cover.
5. My Nom de Plume is going to be RM Calloway.
6. There is room for quirkiness in the design. The book itself is, I may say so, dryly humourous and, also, is set in the future. This allows for a slight twist on more traditional heraldry.
7. It would be nice to include a stylised zodiac wheel that could appear on all the books and the website. It would be one of the motifs that links the books together. In the story, a round table of the zodiac is set up. This is a fusion of astrology and Arthurian legend.
8. My main concern with my own design is the colouring. I was concerned that it looked a little cheap to have a single matt colour. I was thinking that some sort of texture of w/e might add a bit of quality to the design. This is not a deal breaker and, as I said, I would regard it as a safe option if the above change is made.
9. My perfect design would be more like an ACTUAL shield with elements of classic heraldry but a a subtle nod to dystopian rust saint / ashen trials type art work.
Updates
Reason: I have one very strong contender but several other strong drafts on the table and want to give them a chance to improve their designs.
Target Market(s)
Western Teenagers who read fantasy novels such as KOTW, crown of embers, Milo Brackwind etc
Industry/Entity Type
Graphic Design

```html
<!DOCTYPE html>
<html lang="en">
<head>
<meta charset="UTF-8">
<title>Chronicles of the Lanterns - The Heron's Vigil</title>
<link href="https://fonts.googleapis.com/css2?family=Cinzel:wght@400;600;700&display=swap" rel="stylesheet">
<style>
  :root {
    --leather-light: #c99a5e;
    --leather-mid: #b07a42;
    --leather-dark: #7a4a24;
    --title-olive: #4a4220;
    --title-shadow: #2a2210;
    --series-white: #fbf5ea;
    --ring-brown: #8a4f24;
    --motto-brown: #5a2e14;
    --band-green: #3f6b4a;
    --band-edge: #141a12;
    --glyph-ink: #1c1a14;
  }
  * { margin: 0; padding: 0; box-sizing: border-box; }
  html, body { width: 750px; height: 1200px; overflow: hidden; }
  body { background: var(--leather-mid); }

  .cover {
    position: relative;
    width: 750px;
    height: 1200px;
    overflow: hidden;
    background:
      radial-gradient(ellipse 60% 40% at 50% 45%, rgba(230,180,110,0.45), transparent 70%),
      radial-gradient(ellipse 50% 30% at 10% 75%, rgba(60,30,10,0.35), transparent 70%),
      radial-gradient(ellipse 40% 30% at 85% 20%, rgba(90,50,20,0.3), transparent 70%),
      linear-gradient(160deg, var(--leather-light) 0%, var(--leather-mid) 50%, var(--leather-dark) 100%);
    font-family: 'Cinzel', serif;
  }

  .glyph-row {
    position: absolute;
    left: 0;
    top: 32px;
    width: 750px;
    height: 52px;
    background: linear-gradient(90deg, rgba(28,26,20,0.35), rgba(28,26,20,0.55), rgba(28,26,20,0.35));
    opacity: 0.55;
  }

  .series-name {
    position: absolute;
    top: 118px;
    width: 100%;
    text-align: center;
    color: var(--series-white);
    font-size: 30px;
    font-weight: 400;
    letter-spacing: 6px;
  }

  .book-title {
    position: absolute;
    top: 210px;
    width: 100%;
    text-align: center;
    color: var(--title-olive);
    font-weight: 700;
    line-height: 1;
    text-shadow: 1px 1px 0 rgba(255,230,180,0.35), -1px -1px 0 var(--title-shadow);
  }
  .book-title .title-lead { display: block; font-size: 84px; }
  .book-title .title-main { display: block; font-size: 76px; margin-top: 14px; letter-spacing: 1px; }

  .emblem {
    position: absolute;
    left: 0;
    top: 430px;
    width: 750px;
    height: 480px;
  }

  .author-name {
    position: absolute;
    top: 955px;
    width: 100%;
    text-align: center;
    color: var(--title-olive);
    font-size: 78px;
    font-weight: 700;
    letter-spacing: 1px;
    text-shadow: 1px 1px 0 rgba(255,230,180,0.35), -1px -1px 0 var(--title-shadow);
  }

  .base-band {
    position: absolute;
    left: 0;
    top: 1083px;
    width: 750px;
    height: 54px;
    background: var(--band-green);
    border-top: 4px solid var(--band-edge);
    border-bottom: 4px solid var(--band-edge);
  }
  .base-band .band-glyphs {
    position: absolute;
    left: 178px;
    top: 12px;
    width: 394px;
    height: 22px;
    background: var(--glyph-ink);
    opacity: 0.45;
  }
</style>
</head>
<body>
  <main class="cover">
    <div class="glyph-row" role="img" aria-label="Row of ancient cuneiform-style glyphs"></div>

    <p class="series-name">CHRONICLES OF THE LANTERNS</p>

    <h1 class="book-title">
      <span class="title-lead">THE</span>
      <span class="title-main">HERON’S VIGIL</span>
    </h1>

    <svg class="emblem" viewBox="0 0 750 480" xmlns="http://www.w3.org/2000/svg">
      <defs>
        <path id="motto-arc" d="M 148,230 A 227 227 0 0 0 602,230" />
      </defs>
      <circle class="emblem-ring" cx="375" cy="230" r="192" fill="none" stroke="var(--ring-brown)" stroke-width="20" opacity="0.85"/>
      <circle class="emblem-illustration" cx="375" cy="215" r="120" fill="var(--leather-dark)" opacity="0.35" role="img" aria-label="Engraved head of a horned goat"/>
      <text class="motto" font-family="Cinzel, serif" font-weight="700" font-size="25" letter-spacing="8" fill="var(--motto-brown)">
        <textPath href="#motto-arc" startOffset="50%" text-anchor="middle">BEND THE RIVER BACK</textPath>
      </text>
    </svg>

    <p class="author-name">RM CALLOWAY</p>

    <div class="base-band">
      <div class="band-glyphs" role="img" aria-label="Row of ancient cuneiform-style glyphs"></div>
    </div>
  </main>
</body>
</html>
```